Bluebird Business Card Design

Name Marlene Obadofor
Title Mortgage Originator
Office (800) 416-2795 x65
Direct (240) 615-2079
Email mobadofor@bluebirdlending.example
NMLS 3817465
Licensed MD

Name Dorian Pelletier
Title Mortgage Originator
Office (800) 416-2795 x66
Direct (404) 263-5147
Email dpelletier@bluebirdlending.example
NMLS 3156702
Licensed MD

Name Rochelle Barnaby
Title Mortgage Originator
Office (800) 416-2795 x67
Direct (443) 812-3659
Email barnabyrochelle@mailpost.example
NMLS 3902576
Licensed MD

Name Omar Teldouri
Title Mortgage Originator
Office (800) 416-2795 x32
Direct (571) 326-7045
Email oteldouri@bluebirdlending.example
NMLS 1573064
Licensed MD

```html
<!DOCTYPE html>
<html lang="en">
<head>
<meta charset="utf-8">
<title>Bluebird Business Cards</title>
<link href="https://fonts.googleapis.com/css2?family=Manrope:wght@400;500;600;700&display=swap" rel="stylesheet">
<style>
  :root {
    --canvas: #ececed;
    --card-black: #0a0a0b;
    --gold-dark: #b08a1e;
    --gold-mid: #d9b63c;
    --gold-light: #f6ec9c;
    --text-white: #f4f1ea;
    --title-ivory: #e6e0cf;
  }
  * { margin: 0; padding: 0; box-sizing: border-box; }
  html, body { width: 1200px; height: 731px; overflow: hidden; background: var(--canvas); }
  body { position: relative; font-family: "Manrope", Arial, sans-serif; }
  .defs { position: absolute; width: 0; height: 0; }

  .card {
    position: absolute;
    width: 520px;
    height: 298px;
    background: var(--card-black);
    overflow: hidden;
  }
  .card--tl { left: 61px;  top: 48px; }
  .card--tr { left: 614px; top: 48px; }
  .card--bl { left: 62px;  top: 383px; }
  .card--br { left: 615px; top: 383px; }

  .card__art { position: absolute; inset: 0; }

  .name {
    position: absolute;
    left: 221px;
    top: 54px;
    font-size: 25px;
    font-weight: 600;
    letter-spacing: -1.2px;
    line-height: 1;
    background: linear-gradient(180deg, var(--gold-light) 0%, var(--gold-mid) 55%, var(--gold-dark) 100%);
    -webkit-background-clip: text;
    background-clip: text;
    color: transparent;
    padding-bottom: 5px;
    border-bottom: 1.5px solid var(--gold-mid);
    white-space: nowrap;
  }
  .title {
    position: absolute;
    left: 222px;
    top: 89px;
    font-size: 12.5px;
    font-weight: 500;
    color: var(--title-ivory);
    letter-spacing: 0.2px;
  }
  .contacts { position: absolute; left: 224px; top: 129px; list-style: none; }
  .contact {
    position: relative;
    height: 26px;
    display: flex;
    align-items: center;
    font-size: 12.5px;
    font-weight: 500;
    color: var(--text-white);
    white-space: nowrap;
    letter-spacing: 0.1px;
  }
  .contact svg { width: 18px; height: 18px; margin-right: 10px; flex: none; }
  .contact--nmls { align-items: flex-start; height: auto; padding-top: 3px; line-height: 18px; }
  .contact--nmls svg { margin-right: 8px; }
</style>
</head>
<body>

<svg class="defs" aria-hidden="true">
  <defs>
    <linearGradient id="goldBand" x1="0" y1="0" x2="1" y2="0">
      <stop offset="0" stop-color="#b48d22"/>
      <stop offset="0.45" stop-color="#d8b844"/>
      <stop offset="0.7" stop-color="#f7ee9f"/>
      <stop offset="1" stop-color="#c29a2c"/>
    </linearGradient>
    <linearGradient id="goldArea" x1="0" y1="0" x2="0" y2="1">
      <stop offset="0" stop-color="#c9a43a"/>
      <stop offset="0.5" stop-color="#8a6a2c"/>
      <stop offset="1" stop-color="#b08a1e"/>
    </linearGradient>
    <linearGradient id="goldIcon" x1="0" y1="0" x2="0" y2="1">
      <stop offset="0" stop-color="#f6e68e"/>
      <stop offset="1" stop-color="#c49a27"/>
    </linearGradient>

    <g id="cardBands">
      <rect x="0" y="0" width="140" height="7" fill="url(#goldBand)"/>
      <polygon points="136,0 520,0 520,19 156,19" fill="url(#goldBand)"/>
      <rect x="0" y="291" width="148" height="7" fill="url(#goldBand)"/>
      <polygon points="168,279 520,279 520,298 144,298" fill="url(#goldBand)"/>
    </g>

    <g id="iconPhone">
      <circle cx="9" cy="9" r="9" fill="url(#goldIcon)"/>
      <path d="M5.2 4.6c.6-.5 1.4-.4 1.8.2l1 1.6c.3.5.2 1.1-.2 1.5l-.7.6c.6 1.3 1.6 2.3 2.9 2.9l.6-.7c.4-.4 1-.5 1.5-.2l1.6 1c.6.4.7 1.2.2 1.8l-.7.8c-.6.6-1.6.8-2.4.4-2.8-1.2-4.9-3.3-6.1-6.1-.4-.8-.2-1.8.4-2.4z" fill="#0a0a0b"/>
    </g>
    <g id="iconMail">
      <circle cx="9" cy="9" r="9" fill="url(#goldIcon)"/>
      <rect x="4.2" y="5.6" width="9.6" height="6.8" rx="0.8" fill="none" stroke="#0a0a0b" stroke-width="1.3"/>
      <path d="M4.6 6.2 9 9.6l4.4-3.4M4.6 11.8l3.2-2.8M13.4 11.8l-3.2-2.8" fill="none" stroke="#0a0a0b" stroke-width="1.1"/>
    </g>
    <g id="iconPin">
      <circle cx="9" cy="9" r="9" fill="url(#goldIcon)"/>
      <path d="M9 3.6c-2.3 0-4 1.7-4 3.9 0 2.8 4 7 4 7s4-4.2 4-7c0-2.2-1.7-3.9-4-3.9z" fill="#0a0a0b"/>
      <circle cx="9" cy="7.5" r="1.6" fill="url(#goldIcon)"/>
    </g>
  </defs>
</svg>

<!-- Dorian Pelletier -->
<section class="card card--tl">
  <svg class="card__art" viewBox="0 0 520 298">
    <use href="#cardBands"/>
    <rect x="42" y="35" width="124" height="228" rx="10" fill="url(#goldArea)" role="img" aria-label="Gold key illustration framing a portrait photo of Dorian Pelletier"/>
  </svg>
  <h2 class="name" style="text-transform:uppercase">Dorian Pelletier</h2>
  <p class="title">Mortgage Originator</p>
  <ul class="contacts">
    <li class="contact"><svg viewBox="0 0 18 18"><use href="#iconPhone"/></svg>Office (800) 416-2795 x66</li>
    <li class="contact"><svg viewBox="0 0 18 18"><use href="#iconPhone"/></svg>Direct (404) 263-5147</li>
    <li class="contact"><svg viewBox="0 0 18 18"><use href="#iconMail"/></svg>dpelletier@bluebirdlending.example</li>
    <li class="contact contact--nmls"><svg viewBox="0 0 18 18"><use href="#iconPin"/></svg><span>NMLS 3156702<br>Licensed MD</span></li>
  </ul>
</section>

<!-- Omar Teldouri -->
<section class="card card--tr">
  <svg class="card__art" viewBox="0 0 520 298">
    <use href="#cardBands"/>
    <rect x="42" y="35" width="124" height="228" rx="10" fill="url(#goldArea)" role="img" aria-label="Gold key illustration framing a portrait photo of Omar Teldouri"/>
  </svg>
  <h2 class="name">Omar Teldouri</h2>
  <p class="title">Mortgage Originator</p>
  <ul class="contacts">
    <li class="contact"><svg viewBox="0 0 18 18"><use href="#iconPhone"/></svg>Office (800) 416-2795 x32</li>
    <li class="contact"><svg viewBox="0 0 18 18"><use href="#iconPhone"/></svg>Direct (571) 326-7045</li>
    <li class="contact"><svg viewBox="0 0 18 18"><use href="#iconMail"/></svg>oteldouri@bluebirdlending.example</li>
    <li class="contact contact--nmls"><svg viewBox="0 0 18 18"><use href="#iconPin"/></svg><span>NMLS 1573064<br>Licensed MD</span></li>
  </ul>
</section>

<!-- Rochelle Barnaby -->
<section class="card card--bl">
  <svg class="card__art" viewBox="0 0 520 298">
    <use href="#cardBands"/>
    <rect x="42" y="35" width="124" height="228" rx="10" fill="url(#goldArea)" role="img" aria-label="Gold key illustration framing a portrait photo of Rochelle Barnaby"/>
  </svg>
  <h2 class="name">Rochelle Barnaby</h2>
  <p class="title">Mortgage Originator</p>
  <ul class="contacts">
    <li class="contact"><svg viewBox="0 0 18 18"><use href="#iconPhone"/></svg>Office (800) 416-2795 x67</li>
    <li class="contact"><svg viewBox="0 0 18 18"><use href="#iconPhone"/></svg>Direct (443) 812-3659</li>
    <li class="contact"><svg viewBox="0 0 18 18"><use href="#iconMail"/></svg>barnabyrochelle@mailpost.example</li>
    <li class="contact contact--nmls"><svg viewBox="0 0 18 18"><use href="#iconPin"/></svg><span>NMLS 3902576<br>Licensed MD</span></li>
  </ul>
</section>

<!-- Marlene Obadofor -->
<section class="card card--br">
  <svg class="card__art" viewBox="0 0 520 298">
    <use href="#cardBands"/>
    <rect x="42" y="35" width="124" height="228" rx="10" fill="url(#goldArea)" role="img" aria-label="Gold key illustration framing a portrait photo of Marlene Obadofor"/>
  </svg>
  <h2 class="name">Marlene Obadofor</h2>
  <p class="title">Mortgage Originator</p>
  <ul class="contacts">
    <li class="contact"><svg viewBox="0 0 18 18"><use href="#iconPhone"/></svg>(800) 416-2795 x65</li>
    <li class="contact"><svg viewBox="0 0 18 18"><use href="#iconPhone"/></svg>Direct (240) 615-2079</li>
    <li class="contact"><svg viewBox="0 0 18 18"><use href="#iconMail"/></svg>mobadofor@bluebirdlending.example</li>
    <li class="contact contact--nmls"><svg viewBox="0 0 18 18"><use href="#iconPin"/></svg><span>NMLS 3817465<br>Licensed MD</span></li>
  </ul>
</section>

</body>
</html>
```